LITTLE DESIGN WORK REQUIRED!

UPDATE: WE WEREN'T OVERLY ECSTATIC WITH THE DESIGNS WE WERE RECEIVING SO WE DID MOST OF THE DESIGN WORK OURSELVES...

PLEASE SEE THE NEWLY ATTACHED PPT DOC TO VIEW NEARLY EXACT REPLICAS OF WHAT WE WANT THE SITE TO LOOK LIKE. WE NOW NEED YOUR HELP TO MAKE IT LOOK LIKE SOMETHING WORTHY OF THE WEB.

NO CODING REQUIRED - EXPECTED OUTPUT PSD FILES

Hi everyone!

We're looking for a designer to work their magic for our site! We're a not-for-profit program aimed at helping young people realise their potential!

In the attached PPT file, you'll notice we've already DESIGNED THE ENTIRE SITE IN POWERPOINT. Now, we need YOU to make the small changes we requested in the document as well as design the whole thing in psd.

Any questions, don't hesitate to ask.

Brook-Rise
Updates

We've done about 95% of the design for you. Please fine-tune it. See the newly attached PPT doc for details. 

The best two designs will win. This project closes on Friday - please message us if you are absolutely sure you cannot make the deadline.

Thanks,
Brook-Rise

```html
<!DOCTYPE html>
<html lang="en">
<head>
<meta charset="utf-8">
<title>Brook-Rise</title>
<link href="https://fonts.googleapis.com/css2?family=Open+Sans:wght@300;400;600;700&family=Ubuntu:wght@400;500;700&display=swap" rel="stylesheet">
<style>
:root{
  --page:#f4f5ef;
  --green:#7ab317;
  --green-dark:#5e8d0c;
  --bar-top:#4a4a4a;
  --ink:#222;
  --blue:#2f5d9c;
  --social:#4a67a3;
  --panel:#ffffff;
  --line:#d9d9d9;
  --footer:#232323;
  --footer-bottom:#f1f1f1;
}
*{box-sizing:border-box;margin:0;padding:0}
html,body{width:1200px;height:2571px;overflow:hidden}
body{background:var(--page);font-family:"Ubuntu",sans-serif;color:var(--ink);position:relative}
.abs{position:absolute}
a{color:inherit;text-decoration:none}

/* header */
.top-strip{left:0;top:0;width:1200px;height:12px;background:#3a3f45}
.header{left:0;top:12px;width:1200px;height:160px;background:linear-gradient(#e4e8d8,#f2f3ec)}
.brand{left:132px;top:60px;display:flex;align-items:center;gap:10px;font-family:"Open Sans",sans-serif;font-weight:700;font-size:38px;color:#1d1d1d;letter-spacing:1px}
.brand-dot{width:22px;height:22px;background:var(--green);border-radius:50%}
.quote{left:908px;top:40px;width:180px;font-family:"Open Sans",sans-serif;font-weight:600;font-size:14px;line-height:18px;color:#222}
.quote-by{left:900px;top:78px;font-size:14px;color:var(--green-dark);font-family:"Open Sans",sans-serif}
.share{left:1001px;top:78px;height:20px;padding:0 8px;background:var(--social);color:#fff;font-size:11px;line-height:20px;border-radius:2px;display:flex;gap:5px;align-items:center}
.share i{width:8px;height:8px;background:#fff;display:block}

/* nav */
.nav{left:106px;top:142px;width:988px;height:50px;background:linear-gradient(var(--bar-top),#262626);border-radius:4px;display:flex;align-items:center;padding-left:24px;box-shadow:0 3px 5px rgba(0,0,0,.25)}
.nav a{color:#eee;font-size:13px;font-weight:500;margin-right:72px;letter-spacing:.3px}
.nav a.active{background:#f4f7ea;color:var(--green-dark);padding:4px 8px;border-radius:2px;margin-right:62px}
.search{left:884px;top:152px;width:186px;height:24px;background:#fff;border-radius:12px;display:flex;align-items:center;overflow:hidden}
.search span{flex:1;font-size:11px;color:#999;padding-left:10px}
.search b{width:28px;height:24px;background:var(--green);border-radius:0 12px 12px 0;position:relative}
.search b::after{content:"";position:absolute;left:8px;top:6px;width:8px;height:8px;border:2px solid #fff;border-radius:50%}

/* hero */
.hero{left:120px;top:186px;width:966px;height:328px;
  background:
    radial-gradient(ellipse 140px 200px at 105px 230px,rgba(226,170,130,.95),transparent 70%),
    radial-gradient(ellipse 120px 170px at 270px 130px,rgba(214,158,118,.95),transparent 70%),
    radial-gradient(ellipse 100px 150px at 450px 150px,rgba(232,190,120,.9),transparent 70%),
    radial-gradient(ellipse 90px 140px at 600px 130px,rgba(210,160,120,.9),transparent 70%),
    radial-gradient(ellipse 260px 90px at 560px 320px,rgba(120,140,170,.7),transparent 70%),
    linear-gradient(100deg,#6b4a34 0%,#3a3f48 30%,#cfcac0 55%,#a8b0b4 80%,#dfe2e2 100%)}
.signup{left:771px;top:254px;width:292px;height:188px;background:#fff;border-radius:6px;padding:12px 18px;box-shadow:0 2px 8px rgba(0,0,0,.25);border:3px dashed #d9e3ee}
.signup h3{font-family:"Open Sans",sans-serif;font-weight:400;font-size:27px;color:var(--blue);margin-bottom:10px}
.field{display:flex;align-items:center;justify-content:space-between;font-size:10px;margin-bottom:7px;padding-left:8px}
.field i{width:112px;height:18px;border:1px solid #bbb;display:block}
.signup .go{margin:10px 0 0 auto;width:96px;height:24px;background:linear-gradient(#f2f2f2,#d4d4d4);border:1px solid #aaa;border-radius:3px;font-size:12px;text-align:center;line-height:22px;color:#444}

/* main panel */
.panel{left:120px;top:531px;width:970px;height:1735px;background:var(--panel);border:1px solid #ddd;border-radius:4px}
.welcome{left:134px;top:544px;font-family:"Open Sans",sans-serif;font-weight:300;font-size:37px;color:#222}
.welcome b{color:var(--green);font-weight:600}
.intro{left:134px;top:596px;width:640px;font-size:13px;line-height:20px;color:#333}
.intro b{color:var(--green);font-size:21px;font-family:"Open Sans",sans-serif}
.more{left:134px;top:654px;font-size:13px;font-style:italic;font-weight:500}
.recent{left:132px;top:703px;font-family:"Open Sans",sans-serif;font-weight:300;font-size:34px;color:#333}

.cat{left:132px;width:674px}
.cat-bar{height:43px;background:linear-gradient(#454545,#2d2d2d);border-radius:3px;display:flex;align-items:center;padding-left:10px;color:#fff;font-size:18px;gap:14px;box-shadow:0 6px 6px -4px rgba(0,0,0,.3)}
.cat-icon{width:30px;height:24px;background:#eef3f8;border-radius:3px}
.cards{display:flex;gap:36px;margin-top:26px}
.card{width:318px}
.frame{height:175px;border:1px solid var(--line);padding:8px;background:#fff;box-shadow:0 1px 3px rgba(0,0,0,.08)}
.photo{width:100%;height:100%}
.card h4{font-weight:400;font-size:18px;margin:14px 0 10px}
.card p{font-size:11.5px;font-weight:500;line-height:16px;height:48px;overflow:hidden;color:#333;padding-right:6px}

/* sidebar */
.side-h{left:819px;font-family:"Open Sans",sans-serif;font-weight:400;font-size:31px;color:var(--blue)}
.like-row{left:819px;top:598px;width:252px;display:flex;gap:8px;font-size:10px;line-height:13px;color:#444}
.like-row p{width:160px}
.like{height:20px;padding:0 8px;border:1px solid #9aa9c9;background:#eef1f7;color:var(--social);font-size:10px;line-height:18px;border-radius:2px;white-space:nowrap}
.activity{left:819px;top:641px;width:252px;height:242px;border:1px solid #ccc;background:#fff}
.act-head{height:22px;background:var(--social);color:#fff;font-size:10px;display:flex;justify-content:space-between;align-items:center;padding:0 8px}
.act-item{display:flex;gap:8px;padding:9px 8px 0}
.act-item i{width:22px;height:22px;background:var(--social);flex:none;margin-top:2px}
.act-item div{font-size:10.5px;line-height:12px;color:var(--blue)}
.act-item small{display:block;color:#666;font-size:9.5px;margin-top:3px}
.popular{left:819px;top:980px;width:252px;height:460px;border:1px solid #ccc;background:linear-gradient(#fff,#eee)}
.pop-item{height:114px;border-bottom:1px solid #ddd;padding:14px 10px 0 8px;display:flex;gap:6px;font-size:11px;font-weight:500;line-height:16px;position:relative}
.pop-item:last-child{border:0}
.pop-item b{font-size:15px;font-weight:400}
.pop-item small{position:absolute;right:10px;bottom:14px;font-size:10px;color:#999;font-weight:400}
.team{left:819px;top:1586px;width:252px;height:531px;border:1px solid #ccc;background:linear-gradient(#fff,#ececec)}
.member{padding:16px 10px 0;height:262px}
.member .pic{height:138px}
.member h5{font-weight:400;font-size:12px;margin:10px 0 2px 4px}
.member em{display:block;font-size:10.5px;color:#777;margin-left:4px}
.member span{display:block;font-size:10px;color:#777;margin-top:3px}

/* footer */
.footer{left:0;top:2273px;width:1200px;height:260px;background:var(--footer)}
.flinks{left:134px;top:2290px;list-style:none}
.flinks li{color:#aaa;font-size:12px;height:34px;display:flex;gap:8px;align-items:center}
.flinks li::before{content:"";width:0;height:0;border-left:4px solid var(--green);border-top:3px solid transparent;border-bottom:3px solid transparent}
.fh{font-family:"Open Sans",sans-serif;font-weight:400;font-size:23px;color:#999}
.fsearch{left:509px;top:2325px;width:298px;height:24px;background:#fff;border:1px solid #999}
.btn{background:linear-gradient(#8fcc24,#5e9a0c);color:#fff;font-size:12px;text-align:center;border-radius:2px}
.social{left:509px;top:2432px;display:flex;gap:8px}
.social span{width:38px;height:38px;background:#3b3b3b;border:1px solid #555;border-radius:4px;color:#ccc;font-size:8px;line-height:38px;text-align:center}
.cfield{left:828px;width:236px;background:#fff;font-size:12px;padding:4px 6px;color:#222}
.bottom{left:0;top:2533px;width:1200px;height:38px;background:var(--footer-bottom);font-size:12px;color:#555;text-align:right;padding:10px 116px 0 0}
</style>
</head>
<body>
<div class="abs top-strip"></div>
<header class="abs header"></header>
<div class="abs brand"><span class="brand-dot"></span>Brook-Rise</div>
<p class="abs quote">"What would you do if you knew you could not fail?"</p>
<p class="abs quote-by">- R. Whitfield</p>
<div class="abs share"><i></i>Share</div>

<nav class="abs nav">
  <a class="active">HOME</a><a>ABOUT US</a><a>RESOURCES</a><a>WORKSHOPS</a><a>AMBASSADORS FEATS</a>
</nav>
<div class="abs search"><span>search...</span><b></b></div>

<div class="abs hero" role="img" aria-label="Row of smiling young people giving thumbs up"></div>
<form class="abs signup">
  <h3>Sign up</h3>
  <div class="field">Email Address:<i></i></div>
  <div class="field">Password:<i></i></div>
  <div class="field">Confirm Password<i></i></div>
  <div class="go">Sign up Now</div>
</form>

<main class="abs panel"></main>
<h1 class="abs welcome">Welcome to <b>Brook-Rise</b></h1>
<p class="abs intro"><b>Brook-Rise</b> is a not-for-profit program aimed at helping people – especially young people – set and achieve authentic, meaningful, and audacious goals.</p>
<a class="abs more">» Read More</a>
<h2 class="abs recent">Recent Post</h2>

<section class="abs cat" style="top:754px">
  <div class="cat-bar"><span class="cat-icon"></span>Discover</div>
  <div class="cards">
    <article class="card"><div class="frame"><div class="photo" role="img" aria-label="Climbers on a snowy mountain summit" style="background:radial-gradient(ellipse 90px 60px at 40% 55%,rgba(200,90,40,.85),transparent 70%),linear-gradient(#6f93c4,#c9d8e8 45%,#f4f6f8 70%,#dde4ea)"></div></div><h4>Title A</h4><p>Lorem Ipsum is simply dummy text of the printing and typesetting industry. Lorem Ipsum has been the industry's standard dummy text ever since the 1500s, when an</p></article>
    <article class="card"><div class="frame"><div class="photo" role="img" aria-label="Two young backpackers outdoors" style="background:radial-gradient(ellipse 70px 80px at 30% 45%,rgba(220,170,140,.9),transparent 70%),radial-gradient(ellipse 70px 80px at 62% 40%,rgba(200,60,70,.85),transparent 70%),linear-gradient(120deg,#5e6b3c,#8a7a5a 50%,#2e2e2e)"></div></div><h4>Title B</h4><p>Lorem Ipsum is simply dummy text of the printing and typesetting industry. Lorem Ipsum has been the industry's standard dummy text ever since the 1500s, when an</p></article>
  </div>
</section>

<section class="abs cat" style="top:1137px">
  <div class="cat-bar"><span class="cat-icon"></span>Design</div>
  <div class="cards">
    <article class="card"><div class="frame"><div class="photo" role="img" aria-label="Two friends chatting in a colourful room" style="background:radial-gradient(ellipse 80px 90px at 55% 50%,rgba(230,200,60,.85),transparent 70%),radial-gradient(ellipse 60px 80px at 35% 55%,rgba(210,60,50,.9),transparent 70%),linear-gradient(110deg,#3e7a34,#6aa04a 40%,#d8c69a)"></div></div><h4>Title C</h4><p>Lorem Ipsum is simply dummy text of the printing and typesetting industry. Lorem Ipsum has been the industry's standard dummy text ever since the 1500s, when an</p></article>
    <article class="card"><div class="frame"><div class="photo" role="img" aria-label="Young woman laughing indoors" style="background:radial-gradient(ellipse 90px 90px at 55% 45%,rgba(232,190,160,.95),transparent 70%),linear-gradient(110deg,#6a2e14,#a65a30 45%,#d8b090 80%,#f0e6dc)"></div></div><h4>Title D</h4><p>Lorem Ipsum is simply dummy text of the printing and typesetting industry. Lorem Ipsum has been the industry's standard dummy text ever since the 1500s, when an</p></article>
  </div>
</section>

<section class="abs cat" style="top:1517px">
  <div class="cat-bar"><span class="cat-icon"></span>Build</div>
  <div class="cards">
    <article class="card"><div class="frame"><div class="photo" role="img" aria-label="Man splitting logs with an axe" style="background:radial-gradient(ellipse 40px 60px at 70% 60%,rgba(40,80,180,.9),transparent 70%),radial-gradient(ellipse 120px 80px at 20% 70%,rgba(170,110,60,.95),transparent 70%),linear-gradient(#3f6fc0,#7fa0c8 30%,#7e9a5c 55%,#8c5e34)"></div></div><h4>Title E</h4><p>Lorem Ipsum is simply dummy text of the printing and typesetting industry. Lorem Ipsum has been the industry's standard dummy text ever since the 1500s, when an</p></article>
    <article class="card"><div class="frame"><div class="photo" role="img" aria-label="Two young workers giving thumbs up" style="background:radial-gradient(ellipse 50px 80px at 42% 60%,rgba(40,70,150,.95),transparent 75%),radial-gradient(ellipse 40px 70px at 62% 62%,rgba(60,60,70,.85),transparent 75%),linear-gradient(#fafafa,#eeeeee)"></div></div><h4>Title F</h4><p>Lorem Ipsum is simply dummy text of the printing and typesetting industry. Lorem Ipsum has been the industry's standard dummy text ever since the 1500s, when an</p></article>
  </div>
</section>

<section class="abs cat" style="top:1904px">
  <div class="cat-bar"><span class="cat-icon"></span>Achieve</div>
  <div class="cards">
    <article class="card"><div class="frame"><div class="photo" role="img" aria-label="Friends celebrating together" style="background:radial-gradient(ellipse 70px 70px at 30% 40%,rgba(240,210,170,.95),transparent 70%),radial-gradient(ellipse 60px 60px at 60% 65%,rgba(200,50,80,.85),transparent 70%),linear-gradient(120deg,#3e94c0,#9cc6d8 40%,#e8d2b8 70%,#c44a6a)"></div></div><h4>Title G</h4><p>Lorem Ipsum is simply dummy text of the printing and typesetting industry. Lorem Ipsum has been the industry's standard dummy text ever since the 1500s, when an</p></article>
    <article class="card"><div class="frame"><div class="photo" role="img" aria-label="Hands raising a silver trophy" style="background:radial-gradient(ellipse 90px 60px at 50% 40%,rgba(150,150,155,.9),transparent 70%),radial-gradient(ellipse 60px 30px at 50% 85%,rgba(130,70,40,.8),transparent 70%),linear-gradient(#fbfbfb,#ededed)"></div></div><h4>Title H</h4><p>Lorem Ipsum is simply dummy text of the printing and typesetting industry. Lorem Ipsum has been the industry's standard dummy text ever since the 1500s, when an</p></article>
  </div>
</section>

<h2 class="abs side-h" style="top:548px">Stay In Touch</h2>
<div class="abs like-row"><span class="like">Like</span><p>22 people like this. Be the first of your friends.</p></div>
<aside class="abs activity">
  <div class="act-head"><b>Recently Activity</b><b>Circlr</b></div>
  <div class="act-item"><i></i><div>Calling All enterpreneurs - Come Hack with Us!<small>1,891 people shared this</small></div></div>
  <div class="act-item"><i></i><div>Platform Updates:Improved Dev site, documentation,and more<small>1,891 people shared this</small></div></div>
  <div class="act-item"><i></i><div>Calling All enterpreneurs - Come Hack with Us!<small>1,891 people shared this</small></div></div>
  <div class="act-item"><i></i><div>Platform Updates:Improved Dev site, documentation,and more<small>1,891 people shared this</small></div></div>
</aside>

<h2 class="abs side-h" style="top:928px;left:822px">Popular Posts</h2>
<aside class="abs popular">
  <div class="pop-item"><b>1)</b><p>Lorem Ipsum is simply dummy text of the printing and typesetting industry. Lorem Ipsum has been the industry's</p><small>587 View(s)</small></div>
  <div class="pop-item"><b>2)</b><p>Lorem Ipsum is simply dummy text of the printing and typesetting industry. Lorem Ipsum has been the industry's</p><small>587 View(s)</small></div>
  <div class="pop-item"><b>3)</b><p>Lorem Ipsum is simply dummy text of the printing and typesetting industry. Lorem Ipsum has been the industry's</p><small>587 View(s)</small></div>
  <div class="pop-item"><b>4)</b><p>Lorem Ipsum is simply dummy text of the printing and typesetting industry. Lorem Ipsum has been the industry's</p><small>587 View(s)</small></div>
</aside>

<h2 class="abs side-h" style="top:1512px;left:835px">Get To Know Us</h2>
<aside class="abs team">
  <div class="member"><div class="pic" role="img" aria-label="Portrait of ambassador John Doe" style="background:radial-gradient(ellipse 70px 80px at 55% 55%,rgba(226,180,150,.95),transparent 70%),radial-gradient(ellipse 70px 30px at 55% 18%,rgba(130,90,50,.9),transparent 70%),linear-gradient(120deg,#4f8a2e,#8fbf4a 60%,#bcd88a)"></div><h5>John Doe</h5><em>Young entrepreneur &amp; Brook-Rise Ambassador</em><span>▸ Meet John</span></div>
  <div class="member"><div class="pic" role="img" aria-label="Tennis player Jane Smith on court" style="background:radial-gradient(ellipse 50px 60px at 62% 45%,rgba(220,170,140,.95),transparent 70%),radial-gradient(ellipse 60px 40px at 62% 85%,rgba(110,70,140,.85),transparent 70%),linear-gradient(120deg,#3f6e2e,#6fa04a 50%,#4b7a36)"></div><h5>Jane Smith</h5><em>Professional athlete &amp; Brook-Rise Ambassador</em><span>▸ Meet Jane</span></div>
</aside>

<footer class="abs footer"></footer>
<ul class="abs flinks"><li>Home</li><li>About us</li><li>Resources</li><li>Workshops</li><li>Ambassadors</li><li>Feats</li></ul>
<h3 class="abs fh" style="left:509px;top:2285px">Search</h3>
<div class="abs fsearch"></div>
<div class="abs btn" style="left:509px;top:2358px;width:86px;height:26px;line-height:26px">Search</div>
<h3 class="abs fh" style="left:509px;top:2394px">Follow Us</h3>
<div class="abs social"><span>Circlr</span><span>Chirply</span><span>Tubely</span><span>Linkfold</span></div>
<h3 class="abs fh" style="left:828px;top:2285px">Contact Us</h3>
<div class="abs cfield" style="top:2323px;height:26px">Name:</div>
<div class="abs cfield" style="top:2361px;height:26px">Email:</div>
<div class="abs cfield" style="top:2398px;height:86px">Message:</div>
<div class="abs btn" style="left:830px;top:2496px;width:86px;height:26px;line-height:26px;font-size:15px">Send</div>
<div class="abs bottom">@2012 Brook-Rise All Rights Reserved</div>
</body>
</html>
```